Homemaking training schools needs a Business Card design

Designer, Hello!

No special requirements, good-looking enough.
--------------------------------------------------------------------------

Name: Marcus Liao
Chairman
Tel: 0574-57418263
Mobile: 13852247106
Email: kelvory@mailpond.com
Web: www.tqb2031.com
Add: No.258, LinfengJie, DaoyueQu, Ningbo, Zhejiang

LOGO
Ningbo TQB Homemaking Training School

Target Market(s)

pregnant women, mothers, infants, the elderly and families, including cleaning, cooking, nursing training.

Industry/Entity Type

Business

Contact Information for Business Card

Name: Marcus Liao
Chairman
Tel: 0574-57418263
Mobile: 13852247106
Email: kelvory@mailpond.com
Web: www.tqb2031.com

LOGO

Font styles to use
Serif
Sans Serif
Decorative

Requirements
Nice to have
• Feels: clean, specifications, safety, comfort, warmth and happiness.

```html
<!DOCTYPE html>
<html lang="en">
<head>
<meta charset="utf-8">
<title>TianQiBao Business Card</title>
<link href="https://fonts.googleapis.com/css2?family=Quicksand:wght@400;500;700&display=swap" rel="stylesheet">
<style>
  :root {
    --page-bg: #ece9e4;
    --card-bg: #fdfdfd;
    --brand-blue: #2aa3d8;
    --brand-pink: #e619b4;
    --text-grey: #8a8a8a;
    --text-dark: #5c5c5c;
    --rule-grey: #9a9a9a;
  }
  * { margin: 0; padding: 0; box-sizing: border-box; }
  html, body {
    width: 1200px;
    height: 1023px;
    overflow: hidden;
    background: var(--page-bg);
    font-family: "Quicksand", sans-serif;
  }
  .canvas { position: relative; width: 1200px; height: 1023px; }
  .card {
    position: absolute;
    width: 560px;
    height: 320px;
    background: var(--card-bg);
    border-radius: 14px 56px 14px 56px;
    box-shadow: 0 10px 30px rgba(0,0,0,0.12);
  }
  .card-front { left: 70px; top: 130px; }
  .card-back { left: 570px; top: 560px; }

  .person { position: absolute; left: 44px; top: 150px; }
  .person-name { color: var(--brand-blue); font-weight: 700; font-size: 24px; letter-spacing: 0.3px; }
  .person-title { color: var(--text-grey); font-size: 14px; margin-top: 2px; }

  .contact-list { position: absolute; left: 44px; top: 222px; list-style: none; }
  .contact-item {
    display: flex; align-items: center; gap: 8px;
    color: var(--text-dark); font-size: 15px; line-height: 24px;
  }
  .contact-icon { width: 13px; height: 13px; flex: none; }

  .address {
    position: absolute; left: 300px; top: 232px;
    color: var(--text-grey); font-size: 14px; line-height: 24px;
    text-transform: uppercase; letter-spacing: 0.4px;
  }

  .brand { position: absolute; left: 0; right: 0; top: 92px; text-align: center; }
  .brand-row { display: inline-flex; align-items: center; gap: 10px; }
  .brand-name { color: var(--brand-blue); font-weight: 500; font-size: 50px; letter-spacing: 0.5px; }
  .brand-dot { width: 14px; height: 14px; border-radius: 50%; background: var(--brand-pink); }
  .brand-tagline {
    display: flex; align-items: center; justify-content: center; gap: 12px;
    color: var(--text-grey); font-size: 15px; letter-spacing: 0.8px; margin-top: 6px;
  }
  .brand-tagline::before, .brand-tagline::after {
    content: ""; width: 56px; height: 1px; background: var(--rule-grey);
  }
  .website {
    position: absolute; left: 40px; bottom: 30px;
    color: var(--text-dark); font-size: 13px; letter-spacing: 0.5px;
  }
</style>
</head>
<body>
<div class="canvas">

  <section class="card card-front">
    <div class="person">
      <div class="person-name">Marcus Liao</div>
      <div class="person-title">Chairman</div>
    </div>
    <ul class="contact-list">
      <li class="contact-item">
        <svg class="contact-icon" viewBox="0 0 14 14"><circle cx="7" cy="7" r="7" fill="var(--brand-pink)"/><rect x="4" y="4" width="6" height="6" rx="1" fill="#fff"/></svg>
        0574-57418263
      </li>
      <li class="contact-item">
        <svg class="contact-icon" viewBox="0 0 14 14"><circle cx="7" cy="7" r="7" fill="var(--brand-pink)"/><rect x="5" y="3" width="4" height="8" rx="1" fill="#fff"/></svg>
        13852247106
      </li>
      <li class="contact-item">
        <svg class="contact-icon" viewBox="0 0 14 14"><circle cx="7" cy="7" r="7" fill="var(--brand-pink)"/><rect x="3.5" y="4.5" width="7" height="5" fill="#fff"/><path d="M3.5 4.5 L7 7.5 L10.5 4.5" stroke="var(--brand-pink)" stroke-width="0.8" fill="none"/></svg>
        kelvory@mailpond.com
      </li>
    </ul>
    <div class="address">
      No.258, LinfengJie<br>DaoyueQu, Ningbo, Zhejiang
    </div>
  </section>

  <section class="card card-back">
    <div class="brand">
      <div class="brand-row">
        <span class="brand-name">TianQiBao</span>
        <span class="brand-dot"></span>
      </div>
      <div class="brand-tagline">Training &amp; Services</div>
    </div>
    <div class="website">www.tqb2031.com</div>
  </section>

</div>
</body>
</html>
```